Boat business cards

I'm looking for business cards with the two logos I've attached. I don't have an specific idea in mind and open to anything. All the usual info will be on the card. Name, position in company, nr, email, address, ect. The company rents out these two boats for charters and fishing.

```html
<!DOCTYPE html>
<html lang="en">
<head>
<meta charset="utf-8">
<title>Polar Reverie Charters – Business Card</title>
<link rel="stylesheet" href="https://fonts.googleapis.com/css2?family=Noto+Sans:wght@400;600;700&display=swap">
<style>
  :root {
    --page-bg: #d5d8d9;
    --front-top: #454545;
    --front-bottom: #646464;
    --brand-ink: #111111;
    --back-white: #ffffff;
    --blue-top: #7fa4ce;
    --blue-bottom: #6a88ad;
    --swoosh-gray: #58595b;
    --text-light: #ffffff;
    --text-soft: #eef3f9;
    --boat-name: #4a4b4d;
  }
  * { margin: 0; padding: 0; box-sizing: border-box; }
  html, body {
    width: 1200px; height: 928px; overflow: hidden;
    background: var(--page-bg);
    font-family: "Noto Sans", sans-serif;
  }
  .card {
    position: absolute;
    left: 264px;
    width: 672px;
    height: 384px;
    border-radius: 16px;
    overflow: hidden;
  }
  /* Front */
  .card-front {
    top: 52px;
    background: linear-gradient(180deg, var(--front-top), var(--front-bottom));
  }
  .yacht-art {
    position: absolute;
    left: 178px; top: 125px;
    width: 320px; height: 74px;
    border-radius: 4px;
    background: linear-gradient(180deg, #f2f2f2 0%, #cfcfcf 45%, #8a6d4c 55%, #7a5f40 85%, #6d86b8 100%);
  }
  .front-brand {
    position: absolute;
    left: 0; right: 0; top: 212px;
    text-align: center;
    font-size: 36px;
    font-weight: 700;
    letter-spacing: 1px;
    color: var(--brand-ink);
  }
  /* Back */
  .card-back {
    top: 492px;
    background: var(--back-white);
  }
  .back-shapes { position: absolute; inset: 0; }
  .boat-art {
    position: absolute;
    left: 36px; top: 112px;
    width: 270px; height: 120px;
    border-radius: 4px;
    background: linear-gradient(180deg, #f4f5f7 0%, #dfe3e8 50%, #8fb0d6 70%, #6f95c4 100%);
  }
  .boat-brand {
    position: absolute;
    left: 36px; top: 234px;
    width: 270px;
    text-align: center;
    font-size: 30px;
    font-weight: 700;
    color: var(--boat-name);
  }
  .contact {
    position: absolute;
    left: 399px; top: 78px;
    color: var(--text-light);
  }
  .contact-name { font-size: 27px; font-weight: 700; line-height: 1.2; }
  .contact-role { font-size: 15px; color: var(--text-soft); margin-top: 6px; }
  .contact-address { font-size: 15.5px; line-height: 27px; margin-top: 13px; }
  .contact-lines { list-style: none; margin-top: 10px; font-size: 15.5px; }
  .contact-lines li { display: flex; align-items: center; height: 29px; }
  .contact-lines svg { width: 16px; height: 16px; margin-right: 6px; fill: var(--text-light); }
</style>
</head>
<body>
  <section class="card card-front">
    <div class="yacht-art" role="img" aria-label="Illustration of the Polar Reverie motor yacht"></div>
    <div class="front-brand">Polar Reverie</div>
  </section>

  <section class="card card-back">
    <svg class="back-shapes" viewBox="0 0 672 384" width="672" height="384" aria-hidden="true">
      <defs>
        <linearGradient id="blueFill" x1="0" y1="0" x2="0.3" y2="1">
          <stop offset="0" stop-color="var(--blue-top)"/>
          <stop offset="1" stop-color="var(--blue-bottom)"/>
        </linearGradient>
      </defs>
      <path d="M296,0 Q410,190 260,384 L290,384 Q402,192 298,0 Z" fill="var(--swoosh-gray)"/>
      <path d="M292,0 Q399,192 290,384 L672,384 L672,0 Z" fill="#ffffff"/>
      <path d="M294,0 Q402,192 294,384 L672,384 L672,0 Z" fill="url(#blueFill)"/>
    </svg>

    <div class="boat-art" role="img" aria-label="Illustration of the Tide Runner sport fishing boat"></div>
    <div class="boat-brand">Tide Runner</div>

    <div class="contact">
      <h1 class="contact-name">Maren Holt</h1>
      <p class="contact-role">Director</p>
      <p class="contact-address">4120 Harbor Point Ave<br>Lakeview, OH 45100</p>
      <ul class="contact-lines">
        <li>
          <svg viewBox="0 0 24 24"><path d="M6.6 10.8a15.1 15.1 0 0 0 6.6 6.6l2.2-2.2a1 1 0 0 1 1-.25 11.4 11.4 0 0 0 3.6.57 1 1 0 0 1 1 1V20a1 1 0 0 1-1 1A17 17 0 0 1 3 4a1 1 0 0 1 1-1h3.5a1 1 0 0 1 1 1c0 1.25.2 2.45.57 3.6a1 1 0 0 1-.25 1z"/></svg>
          <span>555-204-1187</span>
        </li>
        <li>
          <svg viewBox="0 0 24 24"><path d="M2 5h20v2l-10 6L2 7z M2 9l10 6 10-6v10H2z"/></svg>
          <span>info@polarreveriecharters.com</span>
        </li>
        <li>
          <svg viewBox="0 0 24 24"><path d="M12 2a10 10 0 1 0 0 20 10 10 0 0 0 0-20zm-1 17.9A8 8 0 0 1 4.1 11H7c.3 1.5 1.4 2 2.5 2.5 1 .5 1.5 1.5 1.5 2.5zM17.9 16.5c-.3-.8-1-1.5-1.9-1.5h-1v-3a1 1 0 0 0-1-1H8V9h2a1 1 0 0 0 1-1V6h2a2 2 0 0 0 2-2v-.4a8 8 0 0 1 2.9 12.9z"/></svg>
          <span>www.polarreveriecharters.com</span>
        </li>
      </ul>
    </div>
  </section>
</body>
</html>
```